Harwick Legal

To update and modernize current business card appearance. Marta's business is based in Melbourne with 4 other lawyers in the firm. Marta travels to the Pilbara in Western Australia approximately 1 week a month as part of the firms legal work. She consults with clients in Newman, Tom Price and Port Hedland. The lawyers work mostly from a home office, apart from court appearances. They have a virtual office in Melbourne city, and use facilities in 3 or 4 other locations around Melbourne. It is important the client's think this is a conventional law firm with a permanent office. Our business structure is a difficult concept for them to grasp. The business has been operational for 3 years, growing from 1 lawyer to 4 lawyers during that time. Our website is www.Harwicklegal.example.au and is currently being upgraded as we are not happy with its content. The logo is currently orange and dark grey but the orange is a difficult colour to reproduce and often turns out "poo" brown when documents are printed. We need clients to know we are user friendly and caring - and not head up our rears ends as some lawyers appear to be.
Updates

Thank you for the feedback so far. 1. Some of the designs have too much black (We prefer darker grey & not too much.) 2. Happy for designers to play around with different colours & logo design. What we're after is a modern look and business card that people say "wow" when they pick it up.

Industry/Entity Type

Business

```html
<!DOCTYPE html>
<html lang="en">
<head>
<meta charset="utf-8">
<title>Harwick Legal – Business Cards</title>
<link rel="stylesheet" href="https://fonts.googleapis.com/css2?family=Cormorant+Garamond:wght@300;400;500;700&family=Lato:wght@400;700&display=swap">
<style>
  :root {
    --backdrop: #e8e8ea;
    --card: #ffffff;
    --ink: #4a4a4c;
    --ink-soft: #7a7a7c;
    --cream: #efe7cf;
    --shadow: rgba(0, 0, 0, 0.10);
  }
  * { box-sizing: border-box; margin: 0; padding: 0; }
  html, body {
    width: 1200px;
    height: 720px;
    overflow: hidden;
    background: var(--backdrop);
  }
  .canvas {
    position: relative;
    width: 1200px;
    height: 720px;
  }
  .card {
    position: absolute;
    top: 201px;
    width: 520px;
    height: 318px;
    background: var(--card);
    box-shadow: 0 6px 22px var(--shadow);
    color: var(--ink);
    overflow: hidden;
  }
  .card--back { left: 50px; }
  .card--front { left: 630px; }

  /* Back: personal details */
  .person {
    position: absolute;
    left: 40px;
    right: 40px;
    top: 42px;
  }
  .person__name {
    font-family: "Cormorant Garamond", serif;
    font-weight: 300;
    font-size: 26px;
    letter-spacing: 0.3em;
    white-space: nowrap;
    line-height: 1.1;
  }
  .person__rule {
    height: 1px;
    background: var(--cream);
    margin: 8px 0 6px;
  }
  .person__credentials {
    font-family: "Lato", sans-serif;
    font-size: 8.5px;
    letter-spacing: 0.14em;
    color: var(--ink-soft);
    text-align: right;
    padding-right: 56px;
  }
  .person__role {
    display: block;
    width: max-content;
    margin: 12px auto 0;
    font-family: "Cormorant Garamond", serif;
    font-weight: 700;
    font-size: 14px;
    letter-spacing: 0.14em;
    border-bottom: 1px solid var(--ink);
    padding-bottom: 2px;
  }
  .person__stars {
    text-align: center;
    font-family: "Cormorant Garamond", serif;
    font-size: 14px;
    letter-spacing: 0.9em;
    color: var(--ink-soft);
    margin-top: 12px;
    padding-left: 0.9em;
  }
  .contact {
    position: absolute;
    left: 40px;
    right: 40px;
    bottom: 40px;
    list-style: none;
    font-family: "Cormorant Garamond", serif;
    font-size: 11px;
    letter-spacing: 0.22em;
    color: var(--ink);
  }
  .contact__item {
    display: flex;
    justify-content: space-between;
    line-height: 22px;
    white-space: nowrap;
  }
  .contact__label {
    font-family: "Lato", sans-serif;
    font-weight: 700;
    font-size: 8px;
    letter-spacing: 0.1em;
  }

  /* Front: firm name */
  .firm {
    position: absolute;
    right: 48px;
    top: 106px;
    display: flex;
    align-items: center;
    gap: 18px;
  }
  .firm__mark {
    width: 22px;
    height: 22px;
    border-radius: 50%;
    background: var(--cream);
  }
  .firm__name {
    font-family: "Cormorant Garamond", serif;
    font-weight: 400;
    font-size: 40px;
    letter-spacing: 0.14em;
    line-height: 1;
    color: var(--ink);
    text-align: right;
  }
  .firm__name span {
    display: block;
    font-size: 17px;
    letter-spacing: 0.3em;
    margin-top: 6px;
  }
  .location {
    position: absolute;
    right: 48px;
    bottom: 40px;
    text-align: right;
    font-family: "Lato", sans-serif;
    color: var(--ink);
  }
  .location__city {
    font-weight: 700;
    font-size: 10px;
    letter-spacing: 0.2em;
  }
  .location__area {
    font-size: 9px;
    letter-spacing: 0.26em;
    color: var(--ink-soft);
    margin-top: 5px;
  }
</style>
</head>
<body>
<main class="canvas">
  <section class="card card--back" aria-label="Card back">
    <div class="person">
      <h1 class="person__name">J. MARTA CALLOWAY</h1>
      <div class="person__rule"></div>
      <p class="person__credentials">LLB (HONS.) ACCREDITED MEDIATOR</p>
      <p class="person__role">PRINCIPAL SOLICITOR</p>
      <p class="person__stars">* * *</p>
    </div>
    <ul class="contact">
      <li class="contact__item"><span class="contact__label">T.</span><span>1300 HARWICK (427 942)</span></li>
      <li class="contact__item"><span class="contact__label">M.</span><span>0400 555 018</span></li>
      <li class="contact__item"><span class="contact__label">E.</span><span>MARTA.CALLOWAY@HARWICKLEGAL.EXAMPLE.AU</span></li>
    </ul>
  </section>

  <section class="card card--front" aria-label="Card front">
    <div class="firm">
      <div class="firm__mark"></div>
      <h2 class="firm__name">HARWICK<span>LEGAL</span></h2>
    </div>
    <div class="location">
      <p class="location__city">MELBOURNE</p>
      <p class="location__area">CITY AND BAYSIDE SUBURBS</p>
    </div>
  </section>
</main>
</body>
</html>
```